Children's Educational Software - Login Screens

We need graphics for some basic login pages. The main requirements are a background image, buttons and background overlay (box for login fields and app icons). Must utilize responsive design for various resolutions and devices. The mock-up file provides an example of the direction we are wanting to go. The app page will require a version of the background that extends down using a solid colour. One idea would be to add some flowers, bees, etc. to help add some life to the bottom half. I like the idea of clouds and grass, but am open to anything.
Updates

Target Market(s)

Elementary teachers and young children

Coding

Coded - Design and coding required

Number of Pages Required

2 page

Font styles to use
Sans Serif

Requirements
Must have
• Responsive design for various resolutions and devices
Nice to have
• clouds, grass, new app icons if current icons don't fit with new design

```html
<!DOCTYPE html>
<html lang="en">
<head>
<meta charset="UTF-8">
<title>BrightSteps – Teacher Login</title>
<link href="https://fonts.googleapis.com/css2?family=Roboto:wght@400;500;700&display=swap" rel="stylesheet">
<style>
  :root {
    --sky: #cff3fd;
    --navy: #1f3c7c;
    --brand: #1d4f9c;
    --text-blue: #3d5a94;
    --field: #f2f2f2;
    --white: #ffffff;
    --back-grey: #b8b8b8;
    --login-green: #74c41a;
    --hill-blue: #5aa7f0;
    --grass: #7dc52a;
    --grass-dark: #5aa51c;
    --accent: #f29a2e;
  }
  * { box-sizing: border-box; margin: 0; padding: 0; }
  html, body {
    width: 675px;
    height: 1200px;
    overflow: hidden;
  }
  body {
    position: relative;
    background: var(--sky);
    font-family: "Roboto", Arial, sans-serif;
  }
  .brand {
    position: absolute;
    top: 72px;
    left: 0;
    width: 675px;
    display: flex;
    justify-content: center;
    align-items: center;
    gap: 14px;
  }
  .brand-mark {
    width: 56px;
    height: 56px;
    background: var(--accent);
    border-radius: 6px;
  }
  .brand-name {
    font-size: 46px;
    font-weight: 700;
    color: var(--brand);
    letter-spacing: -0.5px;
  }
  .login-card {
    position: absolute;
    left: 117px;
    top: 277px;
    width: 448px;
    height: 463px;
    background: var(--white);
    border-radius: 8px;
    overflow: hidden;
  }
  .login-card__header {
    height: 56px;
    background: var(--navy);
    color: var(--white);
    font-size: 23px;
    font-weight: 700;
    display: flex;
    align-items: center;
    justify-content: center;
  }
  .login-card__body {
    padding: 18px 49px 0;
  }
  .login-card__intro {
    font-size: 11.5px;
    color: var(--text-blue);
    text-align: center;
    margin-bottom: 22px;
  }
  .field-label {
    display: block;
    font-size: 11.5px;
    color: var(--text-blue);
    margin-bottom: 6px;
  }
  .field-input {
    display: block;
    width: 350px;
    height: 40px;
    background: var(--field);
    border: none;
    border-radius: 2px;
    margin-bottom: 22px;
  }
  .actions {
    display: flex;
    justify-content: center;
    gap: 13px;
    margin-top: 3px;
  }
  .btn {
    width: 99px;
    height: 39px;
    border: none;
    border-radius: 20px;
    color: var(--white);
    font-family: "Roboto", Arial, sans-serif;
    font-size: 15px;
    font-weight: 700;
  }
  .btn--back { background: var(--back-grey); }
  .btn--login { background: var(--login-green); }
  .help-links {
    display: flex;
    justify-content: center;
    align-items: center;
    gap: 12px;
    margin-top: 28px;
    font-size: 11px;
    color: var(--text-blue);
  }
  .help-links__divider {
    width: 2px;
    height: 16px;
    background: var(--navy);
  }
  .landscape {
    position: absolute;
    left: 0;
    bottom: 0;
    width: 675px;
    height: 170px;
    background: linear-gradient(180deg, var(--sky) 0%, var(--hill-blue) 35%, var(--grass) 70%, var(--grass-dark) 100%);
  }
</style>
</head>
<body>
  <header class="brand">
    <span class="brand-mark"></span>
    <span class="brand-name">BrightSteps</span>
  </header>

  <main class="login-card">
    <h1 class="login-card__header">Teacher Login</h1>
    <div class="login-card__body">
      <p class="login-card__intro">Type your username and password to access the Teacher Dashboard</p>
      <label class="field-label" for="username">User name</label>
      <input class="field-input" id="username" type="text">
      <label class="field-label" for="password">Password</label>
      <input class="field-input" id="password" type="password">
      <div class="actions">
        <button class="btn btn--back" type="button">Back</button>
        <button class="btn btn--login" type="button">Login</button>
      </div>
      <nav class="help-links">
        <span>Quick start guide</span>
        <span class="help-links__divider"></span>
        <span>Support page</span>
      </nav>
    </div>
  </main>

  <div class="landscape" role="img" aria-label="Illustrated landscape of a blue mountain, green grassy hills with small trees, a stream and soft white clouds"></div>
</body>
</html>
```